PowerPoint Design Process Flow for Rare Disease Patient Registries

I have attached a powerpoint presentation I need professional design on. This describes our BRIDGEWAY program and the current process and screenshots are include in the attached file. We would like to keep the process, flow, screenshots and images but need it designed to be more visually appealing while stepping through the process.
Looking for a visual queue that let's the user know what step in the process we are on as we then describe the details of that step. We want to reinforce the 5 steps in the process and keep that on each slide. Suggestions on the initial page where we introduce the process before going into the details.
I have attached an image of a button that we will be using for registration buttons and if you could reflect that kind of shape or look and feel that would be cool. Please check http://www.carelinkhubsample.com to see our colors.
Target Market(s)
patient advocacy organizations that represent rare disease communities. Pharmaceutical companies that sell treatments into the disease community.
Industry/Entity Type
It Professional
Look and feel

```html
<!DOCTYPE html>
<html lang="en">
<head>
<meta charset="utf-8">
<title>CareLink Hub BRIDGEWAY – Slides</title>
<link rel="stylesheet" href="https://fonts.googleapis.com/css2?family=Ubuntu:wght@400;500;700&display=swap">
<style>
:root{
  --navy:#1e5079;
  --green:#6cb533;
  --teal:#1ea6c9;
  --tab:#5b5d60;
  --tab-text:#ffffff;
  --ink:#2c2d2f;
  --muted:#7d8186;
  --bg:#eeeeee;
  --paper:#ffffff;
  --shot-blue:#7f9fe4;
}
*{box-sizing:border-box;margin:0;padding:0}
html,body{width:1200px;height:1000px;overflow:hidden}
body{background:radial-gradient(ellipse at center,#fbfbfb 0%,#e6e6e6 100%);font-family:"Ubuntu",Arial,sans-serif;position:relative}
.slide{position:absolute;left:360px;width:486px;height:364px;background:var(--paper);box-shadow:0 3px 10px rgba(0,0,0,.25);overflow:hidden}
.slide--intro{top:87px}
.slide--promote{top:550px}
.slide__header{position:absolute;left:0;top:0;width:100%;background:var(--navy)}
.slide--intro .slide__header{height:74px}
.slide--promote .slide__header{height:30px}
.slide__rule{position:absolute;left:0;width:100%;height:6px;background:var(--green)}
.slide--intro .slide__rule{top:74px}
.slide--promote .slide__rule{top:30px}
.slide__footer{position:absolute;left:0;bottom:0;width:100%;height:8px;background:var(--green)}
.slide__title{position:absolute;top:22px;width:100%;text-align:center;color:#fff;font-weight:500;font-size:21px;letter-spacing:.5px}
.steps{position:absolute;left:36px;display:flex;gap:7px}
.slide--intro .steps{top:68px}
.slide--promote .steps{top:17px}
.step{width:76px;height:23px;background:var(--tab);color:var(--tab-text);font-size:10px;font-style:italic;font-weight:500;display:flex;align-items:center;justify-content:center;clip-path:polygon(6% 0,100% 0,94% 100%,0 100%);letter-spacing:.3px}
.slide--promote .step{color:#c9cacc}
.step--active{background:var(--teal);color:#fff !important}
.bullets{position:absolute;left:52px;top:124px;list-style:none}
.bullets li{position:relative;padding-left:13px;font-size:11.2px;font-weight:500;color:var(--ink);line-height:14px;margin-bottom:18.5px;max-width:360px}
.bullets li::before{content:"";position:absolute;left:0;top:3px;width:5px;height:5px;border-right:2px solid var(--teal);border-bottom:2px solid var(--teal);transform:rotate(-45deg)}
.brand{position:absolute;right:16px;bottom:17px;display:flex;align-items:center;gap:6px;color:#5f7c99;font-size:11px;letter-spacing:2.4px;font-weight:400}
.brand__mark{width:11px;height:11px;background:#2f8fd0}
.headline{position:absolute;left:35px;top:97px;color:var(--ink)}
.headline__kicker,.headline__tail{font-size:13.5px;font-weight:500;letter-spacing:.4px}
.headline__big{font-size:45px;font-weight:500;color:var(--teal);line-height:44px;letter-spacing:.5px}
.shot{position:absolute;background:#fff;border:1px solid #c8c8c8;box-shadow:2px 3px 6px rgba(0,0,0,.3);overflow:hidden}
.shot::before,.shot::after{content:"";position:absolute;top:0;bottom:0;width:5px;background:var(--shot-blue)}
.shot::before{left:0}.shot::after{right:0}
.shot__bar{position:absolute;left:5px;right:5px;top:0;height:10px;background:#f3f3f3;font-size:3.5px;color:#777;text-align:right;padding:3px 6px 0 0}
.shot__nav{position:absolute;left:5px;right:5px;top:10px;height:6px;background:#8c8c8c}
.shot__nav span{position:absolute;left:2px;top:0;width:12px;height:6px;background:#3c68c5}
.shot__side{position:absolute;left:7px;top:22px;font-size:4.5px;color:#333;line-height:6px}
.shot__side b{display:block;font-size:5px;margin-bottom:2px}
.shot__photo{position:absolute}
.shot__btn{position:absolute;height:4px;background:#3c68c5;color:#fff;font-size:3px;text-align:center}
.shot--a{left:255px;top:58px;width:172px;height:122px}
.shot--b{left:45px;top:196px;width:198px;height:142px}
.shot--c{left:285px;top:193px;width:165px;height:115px}
</style>
</head>
<body>

<section class="slide slide--intro">
  <div class="slide__header"></div>
  <div class="slide__rule"></div>
  <h1 class="slide__title">CareLink Hub BRIDGEWAY</h1>
  <nav class="steps">
    <div class="step">PROMOTE</div><div class="step">COLLECT</div><div class="step">EXTEND</div><div class="step">SHARE</div><div class="step">BRIDGEWAY</div>
  </nav>
  <ul class="bullets">
    <li>INITIALLY SPONSORED BY NORVANE PHARMA</li>
    <li>PROVIDE ADVANCED REGISTRY TO EVEN SMALLEST OF ADVOCACY ORGANIZATIONS</li>
    <li>COLLECT DATA IN A COMMON MANNER, SHARE OPENLY</li>
    <li>ENABLE PAN-DISEASE ANALYSIS AND POST-MARKET SURVEILLANCE</li>
    <li>LAUNCHES PUBLICLY MAY 12TH WITH 20 ORGANIZATIONS</li>
  </ul>
  <div class="brand"><span class="brand__mark"></span>CARELINK HUB</div>
  <div class="slide__footer"></div>
</section>

<section class="slide slide--promote">
  <div class="slide__header"></div>
  <div class="slide__rule"></div>
  <nav class="steps">
    <div class="step step--active">PROMOTE</div><div class="step">COLLECT</div><div class="step">EXTEND</div><div class="step">SHARE</div><div class="step">BRIDGEWAY</div>
  </nav>
  <div class="headline">
    <div class="headline__kicker">REGISTRY PARTNERS</div>
    <div class="headline__big">CONTROL</div>
    <div class="headline__tail">BRANDING AND MESSAGING</div>
  </div>

  <div class="shot shot--a">
    <div class="shot__bar">Username Password</div>
    <div class="shot__nav"><span></span></div>
    <div class="shot__side"><b>Hope Alliance Foundation</b>Join the registry today.</div>
    <div class="shot__photo" role="img" aria-label="Photo of a family outdoors on a sunny meadow" style="left:52px;top:26px;width:108px;height:68px;background:linear-gradient(180deg,#9fd0f2 0%,#cfe8f7 55%,#8cc35a 100%)"></div>
    <div class="shot__btn" style="left:88px;top:98px;width:36px"></div>
  </div>

  <div class="shot shot--b">
    <div class="shot__bar">Username Password</div>
    <div class="shot__nav"><span></span></div>
    <div class="shot__side"><b>RenalHope.org</b>About Us</div>
    <div class="shot__photo" role="img" aria-label="Photo of a grandparent with a child" style="left:62px;top:30px;width:122px;height:78px;background:linear-gradient(135deg,#d8d3cb 0%,#b9a795 60%,#8c98a3 100%)"></div>
    <div class="shot__btn" style="left:102px;top:113px;width:40px"></div>
  </div>

  <div class="shot shot--c">
    <div class="shot__bar">Username</div>
    <div class="shot__nav"><span></span></div>
    <div class="shot__side"><b>Bright Path Registry</b></div>
    <div class="shot__photo" role="img" aria-label="Photo of a researcher working in a laboratory" style="left:54px;top:26px;width:100px;height:62px;background:linear-gradient(135deg,#e8eef2 0%,#bcd0dc 55%,#d9c3b0 100%)"></div>
    <div class="shot__btn" style="left:86px;top:92px;width:32px"></div>
  </div>

  <div class="brand"><span class="brand__mark"></span>CARELINK HUB</div>
  <div class="slide__footer"></div>
</section>

</body>
</html>
```